New Plumbing Company

We are looking for a smart and creative business card design for our new plumbing company. We are looking for creativity and originality in our business cards.

Industry/Entity Type

Plumbing

Contact Information for Business Card

Crestline Plumbing
Peter Halvane
Managing Director
Telephone Number : 0481529604
Email : service@crestlineplumbing.com.au
Website : www.crestlineplumbing.com.au
Lic. 508264K

Colors
0692cd
33a6d7
000000

Requirements
Must have
• I want the business card to be designed on a black background using the blue tones i have selected as seen in the company logo.

```html
<!DOCTYPE html>
<html lang="en">
<head>
<meta charset="utf-8">
<title>Crestline Plumbing – Business Card</title>
<link rel="stylesheet" href="https://fonts.googleapis.com/css2?family=Jost:wght@300;400;500&display=swap">
<style>
  :root {
    --page: #ffffff;
    --card-black: #1b1b1b;
    --card-edge: #2a2a2a;
    --brand-blue: #0692cd;
    --light-blue: #33a6d7;
    --white: #ffffff;
    --muted: #9a9a9a;
  }
  * { box-sizing: border-box; margin: 0; padding: 0; }
  html, body {
    width: 1200px; height: 848px; overflow: hidden;
    background: var(--page);
    font-family: "Jost", "Helvetica Neue", Arial, sans-serif;
  }
  .canvas { position: relative; width: 1200px; height: 848px; }
  .card {
    position: absolute; left: 280px; top: 219px;
    width: 638px; height: 389px; overflow: hidden;
    background: radial-gradient(ellipse at 75% 0%, var(--card-edge), var(--card-black) 60%, #141414);
  }
  .water-photo {
    position: absolute; left: 290px; top: 110px; width: 348px; height: 279px;
    background: radial-gradient(ellipse 55% 45% at 60% 62%, #3c3c3c 0%, #262626 45%, rgba(27,27,27,0) 100%);
  }
  .brand { position: absolute; left: 24px; top: 34px; display: flex; align-items: center; gap: 16px; }
  .brand-mark {
    width: 80px; height: 80px; border-radius: 50%;
    border: 5px solid var(--brand-blue);
  }
  .brand-name {
    font-weight: 400; font-size: 36px; color: var(--brand-blue); letter-spacing: 0.5px;
  }
  .person { position: absolute; left: 28px; top: 200px; }
  .person-name { font-weight: 300; font-size: 27px; color: var(--light-blue); line-height: 1; }
  .person-role {
    margin-top: 12px; font-size: 11px; font-weight: 400; letter-spacing: 1.6px;
    color: var(--white); text-transform: uppercase;
  }
  .contacts { position: absolute; left: 28px; top: 290px; list-style: none; }
  .contact { display: flex; align-items: center; gap: 8px; height: 28px; font-size: 17px; font-weight: 300; color: var(--white); }
  .contact-icon {
    width: 17px; height: 17px; border-radius: 50%; background: var(--brand-blue);
    color: var(--white); font-size: 10px; font-weight: 500;
    display: flex; align-items: center; justify-content: center;
  }
  .licence { position: absolute; right: 27px; top: 347px; font-size: 15px; font-weight: 300; color: var(--muted); }
</style>
</head>
<body>
<div class="canvas">
  <section class="card">
    <div class="water-photo" role="img" aria-label="Dark photograph of a water droplet splashing into still black water with ripples"></div>

    <div class="brand">
      <span class="brand-mark"></span>
      <span class="brand-name">Crestline Plumbing</span>
    </div>

    <div class="person">
      <p class="person-name">Peter Halvane</p>
      <p class="person-role">Managing Director</p>
    </div>

    <ul class="contacts">
      <li class="contact"><span class="contact-icon">T</span>0481529604</li>
      <li class="contact"><span class="contact-icon">E</span>service@crestlineplumbing.com.au</li>
      <li class="contact"><span class="contact-icon">W</span>www.crestlineplumbing.com.au</li>
    </ul>

    <p class="licence">Lic. 508264K</p>
  </section>
</div>
</body>
</html>
```